BrightLedger, The Ultimate Franchise Online Training Platform

Need Roll-up Banner Design measuring 30 x 80 inches, Looking for a design that is clean, professional, not cliche. We’re open to shape motifs like a circle, square, or swoosh—choose what best reinforces motion, strength, or innovation. Consistency is key: this should look great whether it's on a banner, a slide deck, or our letterhead. Our business is serving as a Franchisee e-learning platform providing vetted information from experts, an online library and masterclasses. Uploaded examples of Banner art with correct wording. Wording can be:
THE ULTIMATE FRANCHISEE TOOLKIT
Your 24/7 Edge for Franchise Success
On-Demand Resource Library
Monthly Masterclasses
Direct Access to Industry Experts
“Your Entrepreneurial Edge.”
OR
“Opening your first or your fifth, BrightLedger is your unfair advantage.”
Catapult your learning curve.
Avoid costly mistakes.
Grow with a community that gets it.
Join the Movement. Unlock Your Toolkit Today.
Updates

My apologies to designers I haven´t voted or provided updates for yet. We are still reviewing designs as the last call will be made by the owners and we live in different time zones. Thank you!

Target Market(s)

Business Owners, from small to mid

Industry/Entity Type

Small Business Owners, Franchisees

Font styles to use
Other font styles liked:
• Poppins, Roboto, Garamond, Montserrat, Lato

Colors

Designer to choose colors to be used in the design.

Requirements
Must have
• Consistency in color guide, font and wording
Nice to have
• Open to pretty much fluid designs, simple and uncluttered

```html
<!DOCTYPE html>
<html lang="en">
<head>
<meta charset="utf-8">
<title>BrightLedger – Roll-up Banner</title>
<link rel="stylesheet" href="https://fonts.googleapis.com/css2?family=Montserrat:wght@600;700&family=Open+Sans:wght@400;700&display=swap">
<style>
  :root {
    --backdrop: #737372;
    --banner-bg: #f3f3f3;
    --ink: #2b2b2b;
    --ink-soft: #454545;
    --lime: #a5cd3a;
    --white: #ffffff;
  }
  html, body {
    margin: 0;
    padding: 0;
    width: 958px;
    height: 1200px;
    overflow: hidden;
    background: var(--backdrop);
  }
  .canvas {
    position: relative;
    width: 958px;
    height: 1200px;
    background: var(--backdrop);
  }
  .banner {
    position: absolute;
    left: 299px;
    top: 134px;
    width: 357px;
    height: 953px;
    background: var(--banner-bg);
    overflow: hidden;
  }
  .brand-name {
    position: absolute;
    left: 0;
    width: 100%;
    top: 78px;
    margin: 0;
    text-align: center;
    font-family: "Montserrat", sans-serif;
    font-weight: 600;
    font-size: 40px;
    line-height: 40px;
    color: var(--ink);
  }
  .headline {
    position: absolute;
    left: 0;
    width: 100%;
    top: 185px;
    margin: 0;
    text-align: center;
    font-family: "Montserrat", sans-serif;
    font-weight: 700;
    font-size: 32.5px;
    line-height: 36px;
    letter-spacing: 0.5px;
    color: var(--ink);
  }
  .subhead {
    position: absolute;
    left: 0;
    width: 100%;
    top: 320px;
    margin: 0;
    text-align: center;
    font-family: "Montserrat", sans-serif;
    font-weight: 700;
    font-size: 25px;
    line-height: 29px;
    color: var(--lime);
  }
  .features {
    position: absolute;
    left: 38px;
    top: 407px;
    margin: 0;
    padding: 0;
    list-style: none;
    font-family: "Open Sans", sans-serif;
    font-weight: 400;
    font-size: 16.5px;
    line-height: 23.5px;
    color: var(--ink-soft);
  }
  .features li {
    display: flex;
    align-items: center;
    gap: 14px;
  }
  .features svg { flex: none; }
  .network-art {
    position: absolute;
    left: 46px;
    top: 527px;
    width: 264px;
    height: 242px;
    background: linear-gradient(180deg, #e4efc6 0%, #eef2e4 100%);
  }
  .cta-band {
    position: absolute;
    left: 0;
    top: 821px;
    width: 100%;
    height: 132px;
    background: var(--lime);
  }
  .cta-text {
    margin: 0;
    padding-top: 24px;
    text-align: center;
    font-family: "Open Sans", sans-serif;
    font-weight: 700;
    font-size: 20px;
    line-height: 26px;
    color: var(--white);
  }
</style>
</head>
<body>
<main class="canvas">
  <section class="banner">
    <p class="brand-name">BrightLedger</p>

    <h1 class="headline">THE ULTIMATE<br>FRANCHISEE<br>TOOLKIT</h1>
    <h2 class="subhead">Your 24/7 Edge for<br>Franchise Success</h2>

    <ul class="features">
      <li>
        <svg width="17" height="15" viewBox="0 0 17 15" aria-hidden="true">
          <rect x="1" y="3" width="11" height="11" fill="none" stroke="#a5cd3a" stroke-width="1.4"/>
          <path d="M3.5 8 L6.5 11 L15.5 1.5" fill="none" stroke="#a5cd3a" stroke-width="1.6"/>
        </svg>
        On-Demand Resource Library
      </li>
      <li>
        <svg width="17" height="15" viewBox="0 0 17 15" aria-hidden="true">
          <rect x="1" y="3" width="11" height="11" fill="none" stroke="#a5cd3a" stroke-width="1.4"/>
          <path d="M3.5 8 L6.5 11 L15.5 1.5" fill="none" stroke="#a5cd3a" stroke-width="1.6"/>
        </svg>
        Monthly Masterclasses
      </li>
      <li>
        <svg width="17" height="15" viewBox="0 0 17 15" aria-hidden="true">
          <rect x="1" y="3" width="11" height="11" fill="none" stroke="#a5cd3a" stroke-width="1.4"/>
          <path d="M3.5 8 L6.5 11 L15.5 1.5" fill="none" stroke="#a5cd3a" stroke-width="1.6"/>
        </svg>
        Direct Access to Industry Experts
      </li>
    </ul>

    <div class="network-art" role="img" aria-label="Illustration of a flagship storefront with a star badge connected to three franchise storefronts with green awnings"></div>

    <footer class="cta-band">
      <p class="cta-text">Join the Movement.<br>Unlock Your Toolkit Today!</p>
    </footer>
  </section>
</main>
</body>
</html>
```